We are a specialised ICT Consultancy firm based in Perth, Western Australia. We are looking for an A4 brochure titled “Charting Steady Waters” that we can use. I have created the content we would like for the brochure in the attachment “Charting Steady Waters.docx”.
We would like the following on the brochure:
• A copy of the Australian Flag (can be static or rippling in the wind).
• Our logo
• Must be the Meridian Forge blue theme
I have included copies of similar brochures so the designer can get an idea of the theme we are looking for.

```html
<!DOCTYPE html>
<html lang="en">
<head>
<meta charset="utf-8">
<title>Charting Steady Waters – Meridian Forge Systems</title>
<link href="https://fonts.googleapis.com/css2?family=Lato:wght@400;700;900&family=Poppins:wght@500;700;800&display=swap" rel="stylesheet">
<style>
  :root{
    --navy-deep:#0c1a4f;
    --navy:#142a78;
    --royal:#2347a8;
    --cyan:#1fb6ea;
    --cyan-line:#2a9fd6;
    --white:#ffffff;
    --text:#e9eefb;
    --flag-navy:#1c2a7a;
    --flag-red:#c8202f;
  }
  *{margin:0;padding:0;box-sizing:border-box}
  html,body{width:950px;height:1200px;overflow:hidden;background:var(--navy-deep)}
  .brochure{
    position:relative;width:950px;height:1200px;overflow:hidden;
    background:radial-gradient(ellipse 70% 55% at 50% 42%, #2f55b8 0%, var(--navy) 55%, var(--navy-deep) 100%);
    font-family:"Lato",sans-serif;color:var(--text);
  }
  .flag{position:absolute;top:0}
  .flag--left{left:0}
  .flag--right{right:0}
  .brand-tab{position:absolute;left:0;top:0}
  .brand-name{
    position:absolute;top:58px;left:0;width:950px;text-align:center;
    font-family:"Lato",sans-serif;font-weight:900;font-size:34px;letter-spacing:2px;color:var(--navy);
  }
  .brand-sub{
    position:absolute;top:100px;left:0;width:950px;text-align:center;
    font-family:"Lato",sans-serif;font-weight:900;font-size:13px;letter-spacing:9px;color:var(--navy);
  }
  .title{position:absolute;left:0;width:950px;text-align:center;font-family:"Poppins",sans-serif;line-height:1}
  .title__kicker{top:180px;font-weight:500;font-size:40px;color:var(--white)}
  .title__main{top:222px;font-weight:800;font-size:104px;color:var(--white);letter-spacing:1px}
  .title__accent{top:310px;font-weight:800;font-size:90px;color:var(--cyan)}
  .rule{position:absolute;height:1px;background:linear-gradient(90deg,transparent,var(--cyan-line),transparent)}
  .intro{
    position:absolute;top:402px;left:100px;width:750px;text-align:center;
    font-size:17.5px;line-height:24px;color:var(--white);
  }
  .hl{color:var(--cyan);font-weight:700}
  .section-head{font-weight:900;line-height:1.12;font-size:21.5px;color:var(--white)}
  .section-head span{display:block;color:var(--cyan)}
  .block{position:absolute}
  .block p{font-size:14.2px;line-height:18.6px;color:var(--text)}
  .block p + p{margin-top:10px}
  .block .section-head{margin-bottom:10px}
  .icon-lg{position:absolute}
  .commit-head{font-size:23px;line-height:1.1}
  .commit-lead{font-size:16px;line-height:21px;margin-top:12px;color:var(--white)}
  .commit-list{position:absolute;left:550px;top:690px;width:330px;list-style:none}
  .commit-item{position:relative;height:82px;padding-left:62px;padding-top:6px}
  .commit-item:not(:last-child)::after{
    content:"";position:absolute;left:62px;right:0;bottom:4px;height:1px;background:var(--cyan-line)
  }
  .commit-item svg{position:absolute;left:0;top:8px}
  .commit-item h3{font-weight:900;font-size:14.5px;color:var(--cyan);letter-spacing:.2px}
  .commit-item p{font-size:13.8px;line-height:18px;margin-top:2px;color:var(--text)}
  .footer-band{position:absolute;left:0;top:1010px}
  .footer-text{
    position:absolute;top:1086px;left:0;width:950px;text-align:center;
    font-size:16px;line-height:21px;color:var(--white);
  }
  .footer-url{
    position:absolute;top:1140px;left:0;width:950px;text-align:center;
    font-weight:900;font-size:19px;color:var(--cyan);
  }
</style>
</head>
<body>
<main class="brochure">

  <svg class="flag flag--left" width="300" height="245" viewBox="0 0 300 245" role="img" aria-label="Australian flag waving, top left corner">
    <defs>
      <linearGradient id="flagToneL" x1="0" y1="0" x2="1" y2="1">
        <stop offset="0" stop-color="#b4283e"/>
        <stop offset=".35" stop-color="#2b3a8e"/>
        <stop offset="1" stop-color="#17236a"/>
      </linearGradient>
    </defs>
    <path d="M0 0H210C225 60 250 140 300 165C270 175 250 185 230 200C190 175 160 195 130 220C90 215 40 235 0 245Z" fill="url(#flagToneL)"/>
  </svg>

  <svg class="flag flag--right" width="300" height="245" viewBox="0 0 300 245" role="img" aria-label="Australian flag waving, top right corner">
    <defs>
      <linearGradient id="flagToneR" x1="1" y1="0" x2="0" y2="1">
        <stop offset="0" stop-color="#b4283e"/>
        <stop offset=".35" stop-color="#2b3a8e"/>
        <stop offset="1" stop-color="#17236a"/>
      </linearGradient>
    </defs>
    <path d="M300 0H90C75 60 50 140 0 165C30 175 50 185 70 200C110 175 140 195 170 220C210 215 260 235 300 245Z" fill="url(#flagToneR)"/>
  </svg>

  <svg class="brand-tab" width="950" height="160" viewBox="0 0 950 160" aria-hidden="true">
    <path d="M200 0L252 120Q266 152 300 152H650Q684 152 698 120L750 0Z" fill="var(--cyan)"/>
    <path d="M216 0L264 112Q276 142 306 142H644Q674 142 686 112L734 0Z" fill="var(--white)"/>
  </svg>
  <div class="brand-name">MERIDIAN FORGE</div>
  <div class="brand-sub">SYSTEMS</div>

  <div class="rule" style="left:200px;top:203px;width:140px"></div>
  <div class="rule" style="left:610px;top:203px;width:140px"></div>
  <h1>
    <span class="title title__kicker">CHARTING</span>
    <span class="title title__main">STEADY</span>
    <span class="title title__accent">WATERS</span>
  </h1>
  <div class="rule" style="left:140px;top:355px;width:180px"></div>
  <div class="rule" style="left:630px;top:355px;width:180px"></div>

  <p class="intro">As a <span class="hl">100% Western Australian-owned</span> ICT provider, Meridian Forge Systems delivers top-tier tech solutions with a commitment to ethical sourcing that puts Australia first. By partnering with Meridian Forge, you are keeping your investment local and supporting Australia's future.</p>

  <svg class="icon-lg" style="left:56px;top:528px" width="98" height="92" viewBox="0 0 98 92" aria-hidden="true">
    <circle cx="44" cy="44" r="42" fill="#0d1c55" stroke="var(--cyan)" stroke-width="3"/>
    <circle cx="44" cy="44" r="33" fill="none" stroke="var(--cyan)" stroke-width="3"/>
    <ellipse cx="44" cy="44" rx="15" ry="33" fill="none" stroke="var(--cyan)" stroke-width="3"/>
    <line x1="11" y1="44" x2="77" y2="44" stroke="var(--cyan)" stroke-width="3"/>
    <path d="M17 28H71M17 60H71" stroke="var(--cyan)" stroke-width="3"/>
    <circle cx="72" cy="66" r="22" fill="#0d1c55" stroke="var(--white)" stroke-width="3"/>
    <text x="72" y="75" text-anchor="middle" font-family="Lato,sans-serif" font-weight="900" font-size="26" fill="var(--white)">$</text>
  </svg>

  <section class="block" style="left:172px;top:528px;width:315px">
    <h2 class="section-head">THE CHALLENGE OF<span>BIG TECH TAX AVOIDANCE</span></h2>
    <p>Multinational IT corporations frequently minimise their Australian tax obligations by artificially inflating costs to local subsidiaries. This shifts profits offshore and drastically reduces domestic margins, allowing them to avoid paying their fair share of Australian tax.</p>
    <p>As a local provider, Meridian Forge ensures your ICT spending actively contributes to the Australian tax base and supports national growth.</p>
  </section>

  <div class="icon-lg" style="left:68px;top:760px;width:82px;height:78px;border-radius:18px;background:radial-gradient(circle,#2a4fb0,#13246c)" role="img" aria-label="Outline map of Australia with a tick mark"></div>

  <section class="block" style="left:172px;top:838px;width:320px">
    <h2 class="section-head">THE LOCALLY<span>SOURCED ADVANTAGE</span></h2>
    <p>Meridian Forge is committed to a <span class="hl">100% Australian-owned</span> supply chain. We ensure every dollar spent reinvests directly into our national economy—with all taxes paid straight to the Australian Taxation Office (ATO).</p>
  </section>

  <section class="block" style="left:550px;top:528px;width:330px">
    <h2 class="section-head commit-head">MERIDIAN FORGE'S<span>AUSTRALIAN-FIRST</span><span>COMMITMENT</span></h2>
    <p class="commit-lead">At Meridian Forge, we endeavour to maintain an entirely local supply chain.</p>
  </section>

  <ul class="commit-list">
    <li class="commit-item">
      <svg width="48" height="48" viewBox="0 0 48 48" aria-hidden="true"><circle cx="24" cy="24" r="22" fill="none" stroke="var(--cyan)" stroke-width="1.5"/><path d="M11 22l6-5 6 3 5-3 9 5-7 8-6-3-5 3z" fill="var(--white)"/><path d="M10 20l4 6M38 20l-4 6" stroke="var(--cyan)" stroke-width="3" stroke-linecap="round"/></svg>
      <h3>DISTRIBUTORS</h3>
      <p>Preferencing Australian-owned supply networks.</p>
    </li>
    <li class="commit-item">
      <svg width="48" height="48" viewBox="0 0 48 48" aria-hidden="true"><circle cx="24" cy="24" r="22" fill="none" stroke="var(--cyan)" stroke-width="1.5"/><path d="M24 20l-6 16M24 20l6 16M20 30h8" stroke="var(--white)" stroke-width="2" fill="none"/><circle cx="24" cy="18" r="2.5" fill="var(--white)"/><path d="M17 13a9 9 0 0 0 0 10M31 13a9 9 0 0 1 0 10" stroke="var(--cyan)" stroke-width="2" fill="none"/></svg>
      <h3>TELECOMMUNICATIONS</h3>
      <p>Partnering with local network and telco providers.</p>
    </li>
    <li class="commit-item">
      <svg width="48" height="48" viewBox="0 0 48 48" aria-hidden="true"><circle cx="24" cy="24" r="22" fill="none" stroke="var(--cyan)" stroke-width="1.5"/><rect x="14" y="13" width="20" height="6" rx="1" fill="none" stroke="var(--white)" stroke-width="2"/><rect x="14" y="21" width="20" height="6" rx="1" fill="none" stroke="var(--white)" stroke-width="2"/><rect x="14" y="29" width="20" height="6" rx="1" fill="none" stroke="var(--white)" stroke-width="2"/><path d="M17 16h4M17 24h4M17 32h4" stroke="var(--cyan)" stroke-width="2"/></svg>
      <h3>DATA INFRASTRUCTURE</h3>
      <p>Hosting within Australian-owned data centres.</p>
    </li>
    <li class="commit-item">
      <svg width="48" height="48" viewBox="0 0 48 48" aria-hidden="true"><circle cx="24" cy="24" r="22" fill="none" stroke="var(--cyan)" stroke-width="1.5"/><circle cx="24" cy="18" r="4" fill="var(--white)"/><circle cx="15" cy="21" r="3" fill="var(--white)"/><circle cx="33" cy="21" r="3" fill="var(--white)"/><path d="M16 33a8 8 0 0 1 16 0zM9 32a6 6 0 0 1 9-5M39 32a6 6 0 0 0-9-5" fill="var(--white)"/></svg>
      <h3>STRATEGIC PARTNERS</h3>
      <p>Prioritising collaboration with domestic IT vendors</p>
    </li>
  </ul>

  <svg class="footer-band" width="950" height="190" viewBox="0 0 950 190" aria-hidden="true">
    <defs>
      <linearGradient id="footSheen" x1="0" x2="1">
        <stop offset="0" stop-color="#2a55c0"/>
        <stop offset=".5" stop-color="#dfe6ff"/>
        <stop offset="1" stop-color="#2a55c0"/>
      </linearGradient>
    </defs>
    <path d="M0 15Q475 -20 950 15V190H0Z" fill="#2a4fb8" opacity=".6"/>
    <path d="M0 30Q475 -10 950 30V190H0Z" fill="url(#footSheen)" opacity=".55"/>
    <path d="M0 50Q475 15 950 50V190H0Z" fill="var(--navy-deep)"/>
    <line x1="400" y1="53" x2="448" y2="53" stroke="var(--cyan-line)"/>
    <line x1="488" y1="53" x2="536" y2="53" stroke="var(--cyan-line)"/>
    <circle cx="468" cy="53" r="13" fill="none" stroke="var(--cyan)" stroke-width="1.5"/>
    <circle cx="468" cy="53" r="7" fill="none" stroke="var(--white)" stroke-width="1.5"/>
    <path d="M461 53h14M468 46c-4 4-4 10 0 14M468 46c4 4 4 10 0 14" fill="none" stroke="var(--white)" stroke-width="1.2"/>
  </svg>
  <p class="footer-text">All goods and services provided by Meridian Forge are provided in accordance with<br>our Standard Terms and Conditions available at</p>
  <p class="footer-url">https://www.meridianforgesystems.com.au/t&amp;c</p>

</main>
</body>
</html>
```